Ein gutes einfühlen in mich als Kunde, viel Eigeninitiative und zügiges arbeiten, ich bin sehr zufrieden!
Zielgruppe
Ich bin Coach und führe Gespräche mit Frauen die durch die Situation im Aussen oder Lebensümstände überlastet oder überfordert sind.
Aufgabenstellung
Ich mag ein klares und gleichzeitig liebevoll Frauen einladendes Design. Ich mag kein blau und grau dafür aber warme und natürliche Farben.
Ich brauche auch noch einen doppelseitigen Hochkantflyer
Der Text ist: Gespräche zu zweit - für Seelentrost und innere Harmonie (das ist die erste Idee)

```html
<!DOCTYPE html>
<html lang="de">
<head>
<meta charset="utf-8">
<title>Liesbeth Krommhoof – Visitenkarte</title>
<link rel="stylesheet" href="https://fonts.googleapis.com/css2?family=Montserrat:wght@500;600;700&family=Mulish:wght@400;500&display=swap">
<style>
  :root {
    --page-bg: #f1efed;
    --rose-light: #fde1dd;
    --rose-deep: #eccbc4;
    --paper-white: #ffffff;
    --paper-shade: #f0eff2;
    --ink-mauve: #8a5e56;
    --ink-soft: #9a716a;
    --card-shadow: 0 18px 40px rgba(90, 60, 55, 0.18);
  }
  * { box-sizing: border-box; margin: 0; padding: 0; }
  html, body {
    width: 1200px;
    height: 800px;
    overflow: hidden;
    background: var(--page-bg);
  }
  .canvas {
    position: relative;
    width: 1200px;
    height: 800px;
    display: flex;
    align-items: center;
    justify-content: center;
    gap: 60px;
  }
  .card {
    position: relative;
    width: 510px;
    height: 330px;
    border-radius: 4px;
    box-shadow: var(--card-shadow);
    overflow: hidden;
    color: var(--ink-mauve);
  }

  /* Vorderseite */
  .card--front {
    background: linear-gradient(180deg, var(--rose-light) 0%, var(--rose-deep) 100%);
  }
  .brand-name {
    position: absolute;
    top: 92px;
    left: 0;
    width: 100%;
    text-align: center;
    font-family: "Montserrat", sans-serif;
    font-weight: 600;
    font-size: 30px;
    letter-spacing: 0.02em;
    color: var(--ink-mauve);
  }
  .tagline {
    position: absolute;
    top: 190px;
    left: 150px;
    font-family: "Mulish", sans-serif;
    font-weight: 500;
    font-size: 15px;
    line-height: 1.3;
    color: var(--ink-mauve);
  }

  /* Rückseite */
  .card--back {
    background: linear-gradient(180deg, var(--paper-white) 0%, var(--paper-shade) 100%);
  }
  .name-panel {
    position: absolute;
    top: 0;
    left: 150px;
    width: 230px;
    height: 215px;
    background: linear-gradient(180deg, var(--rose-light) 0%, var(--rose-deep) 100%);
    border-radius: 0 0 26px 26px;
  }
  .person-name {
    position: absolute;
    top: 40px;
    left: 34px;
    font-family: "Montserrat", sans-serif;
    font-weight: 700;
    font-size: 24px;
    line-height: 1.2;
    color: var(--ink-mauve);
  }
  .person-role {
    position: absolute;
    top: 140px;
    left: 112px;
    font-family: "Montserrat", sans-serif;
    font-weight: 600;
    font-size: 16px;
    color: var(--ink-mauve);
  }
  .role-curve {
    position: absolute;
    top: 160px;
    left: 60px;
    width: 160px;
    height: 50px;
  }
  .contact {
    position: absolute;
    top: 238px;
    left: 184px;
    font-family: "Mulish", sans-serif;
    font-size: 13px;
    line-height: 1.35;
    color: var(--ink-soft);
  }
  .contact__phone { margin-top: 14px; }
</style>
</head>
<body>
  <main class="canvas">
    <section class="card card--front" aria-label="Vorderseite">
      <p class="brand-name">Liesbeth Krommhoof</p>
      <p class="tagline">Gespräche zu zweit<br>für Seelentrost und innere Harmonie</p>
    </section>

    <section class="card card--back" aria-label="Rückseite">
      <div class="name-panel">
        <h1 class="person-name">Liesbeth<br>Krommhoof</h1>
        <p class="person-role">Coach</p>
        <svg class="role-curve" viewBox="0 0 160 50" aria-hidden="true">
          <path d="M4 46 C 40 10, 100 2, 156 8" fill="none" stroke="var(--ink-mauve)" stroke-width="1.2"/>
        </svg>
      </div>
      <address class="contact" style="font-style: normal;">
        <p>Lindenhofweg 9</p>
        <p>64385 Reichelsheim</p>
        <p class="contact__phone">Mob: 0157 204-31-985</p>
      </address>
    </section>
  </main>
</body>
</html>
```